Brightwell Sound Screen website

I need a website that looks clean and I have the ability to update on my own with pics and text. Want it to be a very easy to use and interesting site. With designs please give me a desription. Want the feel to be for everyone. My goal with my business is so that everyone can enjoy the modern technology that is around us. Please view my temp site for an idea of pics and text. www.brightwellss.example. I am not happy with this site this is why I am asking for much needed help.
Updates

Project Deadline Extended
Reason: Havent had a chance to site down and view all submissions.

Target Market(s)

Clients/business with some expendable income.

Requirements
Must have
• Want a Home, Services, About Us, Contact Us, Products, Phone Support, and Local Support pages. Must have the ability for me to go in and update pages with text and images. First page will have a sales and a current project sections. Hosting is done on Hostmarra and I need to know how to transfer once site is complete.

```html
<!DOCTYPE html>
<html lang="en">
<head>
<meta charset="utf-8">
<title>Brightwell Sound Screen – Contact Us</title>
<link href="https://fonts.googleapis.com/css2?family=Source+Sans+3:wght@400;600;700&display=swap" rel="stylesheet">
<style>
:root{
  --page:#ffffff;
  --topstrip:#ebebeb;
  --brand-blue:#2a78b5;
  --banner-dark:#0f4a7e;
  --banner-mid:#1f5f96;
  --banner-light:#2e80ba;
  --nav-dark:#1a4a70;
  --nav-light:#2a6a98;
  --nav-active:#123a5a;
  --button:#15466d;
  --heading-blue:#1b5c8c;
  --text:#444444;
  --muted:#888888;
  --soft:#777777;
  --line:#cccccc;
  --footer:#f2f2f2;
  --white:#ffffff;
}
*{box-sizing:border-box;margin:0;padding:0}
html,body{width:1042px;height:1200px;overflow:hidden;background:var(--page)}
body{position:relative;font-family:"Source Sans 3",Arial,sans-serif;color:var(--text)}
.abs{position:absolute}

.top-strip{left:0;top:0;width:1042px;height:15px;background:var(--topstrip)}
.header{left:0;top:15px;width:1042px;height:118px;background:linear-gradient(#ffffff,#f1f1f1)}
.brand{left:45px;top:62px;display:flex;align-items:center;gap:10px}
.brand-dot{width:22px;height:22px;border-radius:50%;background:var(--brand-blue)}
.brand-name{font-size:30px;font-weight:700;color:var(--brand-blue);letter-spacing:.5px}
.header-phone{right:44px;top:32px;font-size:25px;font-weight:700;color:var(--brand-blue);letter-spacing:.3px}
.search{left:780px;top:83px;width:225px;height:27px;border:1px solid #d6d6d6;border-radius:5px;background:var(--white);box-shadow:0 6px 6px -4px rgba(0,0,0,.18);font-size:12px;color:#999;padding:6px 10px}
.search svg{position:absolute;right:8px;top:5px}

.banner{left:0;top:133px;width:1042px;height:339px;background:linear-gradient(100deg,var(--banner-mid) 0%,var(--banner-light) 55%,var(--banner-dark) 100%)}
.hero-frame{left:37px;top:148px;width:560px;height:310px;border:4px solid var(--white);box-shadow:0 8px 12px rgba(0,0,0,.35)}
.hero-photo{width:100%;height:100%;background:linear-gradient(180deg,#c9a37a 0%,#d8b58a 55%,#6b3a22 78%,#3b2218 100%)}
.hero-title{left:631px;top:173px;font-size:30px;color:var(--white);font-weight:400;border-bottom:1px solid rgba(255,255,255,.5);padding-bottom:1px}
.hero-tag{left:631px;top:209px;font-size:22px;color:#cfe1f0}
.hero-copy{left:631px;top:249px;width:360px;font-size:12px;line-height:18px;color:var(--white)}
.hero-copy p{margin-bottom:6px}
.read-more{left:638px;top:362px;width:101px;height:29px;border-radius:5px;background:var(--button);color:var(--white);font-size:12px;line-height:29px;text-align:center}
.dots{left:643px;top:434px;display:flex;gap:5px}
.dots span{width:10px;height:10px;border-radius:50%;background:var(--white)}

.nav{left:156px;top:473px;width:731px;height:37px;border-radius:0 0 4px 4px;background:linear-gradient(var(--nav-light),var(--nav-dark));display:flex}
.nav a{color:var(--white);text-decoration:none;font-size:15px;line-height:37px;text-align:center;border-right:1px solid rgba(255,255,255,.18)}
.nav a:last-child{border-right:none}
.nav a.active{background:var(--nav-active)}

.page-title{left:63px;top:540px;font-size:18px;color:var(--heading-blue)}
.form-title{left:62px;top:582px;font-size:18px;color:var(--muted)}
.contact-form label{position:absolute;left:62px;font-size:12px;color:var(--text)}
.contact-form .field{position:absolute;left:62px;width:249px;height:21px;border:1px solid #bfbfbf;background:var(--white)}
.submit{left:114px;top:861px;width:105px;height:22px;border-radius:8px;background:var(--button);color:var(--white);font-size:13px;line-height:22px;text-align:center;box-shadow:0 8px 6px -5px rgba(0,0,0,.3)}
.divider{left:479px;top:591px;width:1px;height:320px;background:#dcdcdc}
.map{left:501px;top:608px;width:257px;height:257px;border:1px solid var(--line);background:linear-gradient(135deg,#ecebe6,#e2e0d8)}
.details-icon{left:792px;top:730px;width:27px;height:27px;border-radius:4px;background:#d9d9d9}
.details-title{left:832px;top:732px;font-size:18px;color:#555}
.details{left:798px;top:772px;font-size:11.5px;line-height:24px;color:var(--text)}

.footer{left:0;top:961px;width:1042px;height:239px;background:var(--footer)}
.f-col{top:972px}
.f-col h3{font-size:16px;font-weight:400;color:#555;margin-bottom:20px}
.f-col li{list-style:none;font-size:11px;color:var(--soft);line-height:23px}
.f-sep{top:970px;width:0;height:175px;border-left:1px dotted #bdbdbd}
.socials{left:575px;top:1005px;display:flex;gap:4px}
.socials span{width:22px;height:22px;border-radius:3px}
.social-links{left:576px;top:1043px;font-size:11.5px;color:var(--soft)}
.f-rule{left:37px;top:1145px;width:971px;height:1px;background:#d4d4d4}
.copyright{left:27px;top:1165px;font-size:11px;color:var(--soft)}
</style>
</head>
<body>
<div class="abs top-strip"></div>
<header class="abs header"></header>
<div class="abs brand"><span class="brand-dot"></span><span class="brand-name">Brightwell Sound Screen</span></div>
<div class="abs header-phone">000 5550 1234</div>
<div class="abs search">type your word here
  <svg width="16" height="16" viewBox="0 0 16 16"><circle cx="6.5" cy="6.5" r="4.5" fill="none" stroke="#bbb" stroke-width="2"/><line x1="10" y1="10" x2="15" y2="15" stroke="#bbb" stroke-width="3"/></svg>
</div>

<section class="abs banner"></section>
<div class="abs hero-frame"><div class="hero-photo" role="img" aria-label="Photo of a boardroom with a long table, leather chairs and a wall-mounted video conference screen"></div></div>
<h1 class="abs hero-title">Brightwell Sound /Screen</h1>
<div class="abs hero-tag">Punch line Goes here</div>
<div class="abs hero-copy">
  <p>Lumora eSolutions is a web service company, offering a wide range of services which range from designing and development, that is covering almost all the fields in the best possible way.</p>
  <p>To be the best we know what and how to present beautifully the working of the client's need and their advantages be highlighted.</p>
</div>
<div class="abs read-more">READ MORE &#8250;</div>
<div class="abs dots"><span></span><span></span><span></span><span></span></div>

<nav class="abs nav">
  <a href="#" style="width:95px">Home</a>
  <a href="#" class="active" style="width:103px">About Us</a>
  <a href="#" style="width:78px">Services</a>
  <a href="#" style="width:77px">Gallery</a>
  <a href="#" style="width:88px">Contact Us</a>
  <a href="#" style="width:157px">Packaged Solutions</a>
  <a href="#" style="width:133px">Help Us Support</a>
</nav>

<h2 class="abs page-title">Contact Us</h2>
<div class="abs form-title">Kindly post your valuable Suggestions &amp; Query</div>
<form class="contact-form">
  <label style="top:625px">Enter your Name</label>
  <div class="field" style="top:644px"></div>
  <label style="top:674px">Enter your Email</label>
  <div class="field" style="top:695px"></div>
  <label style="top:723px">Enter your Phone Number</label>
  <div class="field" style="top:746px"></div>
  <label style="top:772px">Add Your Comments Here:</label>
  <div class="field" style="top:789px;height:48px"></div>
</form>
<div class="abs submit">Submit Query</div>
<div class="abs divider"></div>
<div class="abs map" role="img" aria-label="Street map showing the office location with a pin marker"></div>
<div class="abs details-icon"></div>
<div class="abs details-title">Contact Details</div>
<div class="abs details">
  #12 Harlow Road, Lorem ipsum,<br>
  Phone: +00 555 013 221<br>
  Tollfree: (000) 55501234<br>
  E-mail: info@brightwellss.example
</div>

<footer class="abs footer"></footer>
<div class="abs f-col" style="left:37px"><h3>Our Company</h3><ul><li>Main Page</li><li>About Our Company</li><li>Recent Blog &amp; Comments</li></ul></div>
<div class="abs f-sep" style="left:189px"></div>
<div class="abs f-col" style="left:222px"><h3>About Us</h3><ul><li>Why We Are</li><li>What We Do</li><li>Support &amp; Services</li></ul></div>
<div class="abs f-sep" style="left:352px"></div>
<div class="abs f-col" style="left:376px"><h3>Services Overview</h3><ul><li>Our First Services</li><li>Second Services</li><li>Thrid Services here</li><li>Our Fouth Services</li></ul></div>
<div class="abs f-sep" style="left:536px"></div>
<div class="abs f-col" style="left:576px"><h3>Get In Touch</h3></div>
<div class="abs socials"><span style="background:#3aa0dc"></span><span style="background:#1d6fa8"></span><span style="background:#3b5c9c"></span><span style="background:#4a88d8"></span></div>
<div class="abs social-links">Friendbook &nbsp;|&nbsp; Linkwise &nbsp;|&nbsp; Chirper &nbsp;|&nbsp; Searchly</div>
<div class="abs f-rule"></div>
<div class="abs copyright">copyright © 2012 Company Name | &nbsp; All right reserved</div>
</body>
</html>
```